Business Card and compnay logo

new company for supply and installation of sanitary wares, bathroom accessories and plumping services. company name (silverpine thresholds).

```html
<!DOCTYPE html>
<html lang="en">
<head>
<meta charset="utf-8">
<title>Silverpine Thresholds – Business Card</title>
<link href="https://fonts.googleapis.com/css2?family=Roboto:wght@400;500;700;900&display=swap" rel="stylesheet">
<style>
  :root{
    --backdrop:#2b2b2d;
    --card:#ffffff;
    --blue:#2f74bd;
    --blue-light:#4a8bd0;
    --blue-dark:#175797;
    --ink:#1f2328;
    --muted:#3c4047;
    --band:#3a3b3e;
  }
  *{margin:0;padding:0;box-sizing:border-box}
  html,body{width:1200px;height:800px;overflow:hidden}
  body{
    background:var(--backdrop);
    font-family:"Roboto",Arial,sans-serif;
    position:relative;
  }
  .card{
    position:absolute;
    left:366px;
    width:468px;
    height:266px;
    background:var(--card);
    border-radius:12px;
    overflow:hidden;
    box-shadow:0 8px 18px rgba(0,0,0,.45);
  }
  .card--front{top:101px}
  .card--back{top:427px}

  .front-panel{position:absolute;inset:0;width:100%;height:100%}

  .holder{position:absolute;left:16px;top:50px}
  .holder__name{font-size:19px;font-weight:700;color:var(--ink);line-height:1}
  .holder__name span{color:var(--blue);font-weight:500}
  .holder__role{font-size:10.5px;color:var(--blue);margin-top:4px}

  .contact{position:absolute;left:16px;top:139px;font-size:10.5px;color:var(--muted);line-height:1.4}
  .contact__address{margin-bottom:12px}
  .contact__row{display:flex;align-items:center;gap:6px;height:18px}
  .contact__row svg{width:9px;height:9px;flex:none}
  .contact__rule{height:1.5px;background:var(--blue);margin:2px 0 3px}
  .contact__rule--long{width:197px}
  .contact__rule--short{width:197px}

  .brand{position:absolute;text-align:center}
  .brand__dot{display:block;margin:0 auto 14px;border-radius:50%}
  .brand__name{font-weight:900;letter-spacing:.5px;line-height:1.15;text-transform:uppercase}

  .brand--front{left:260px;top:78px;width:170px}
  .brand--front .brand__dot{width:44px;height:44px;background:#ffffff}
  .brand--front .brand__name{color:#ffffff;font-size:15px}

  .brand--back{left:0;right:0;top:66px}
  .brand--back .brand__dot{width:56px;height:56px;background:var(--blue)}
  .brand--back .brand__name{color:var(--blue);font-size:18px}

  .back-stripe{position:absolute;left:0;right:0;top:231px;height:6px;background:var(--blue)}
  .back-band{position:absolute;left:0;right:0;top:240px;bottom:0;background:var(--band)}
</style>
</head>
<body>

<section class="card card--front">
  <svg class="front-panel" viewBox="0 0 468 266" preserveAspectRatio="none" aria-hidden="true">
    <defs>
      <linearGradient id="panelGrad" x1="0" y1="0" x2="0" y2="1">
        <stop offset="0" stop-color="#4a8bd0"/>
        <stop offset="1" stop-color="#175797"/>
      </linearGradient>
    </defs>
    <polygon points="181,0 468,0 468,266 266,266" fill="url(#panelGrad)"/>
  </svg>

  <div class="holder">
    <div class="holder__name">Daniel <span>Orwell</span></div>
    <div class="holder__role">Marketing &amp; Strategy</div>
  </div>

  <div class="contact">
    <div class="contact__address">L12, 48 Harbour Lane, Sydney<br>NSW 2000</div>
    <div class="contact__row">
      <svg viewBox="0 0 10 10"><rect x="2.5" y="0.5" width="5" height="9" rx="1" fill="none" stroke="#2f74bd" stroke-width="1"/></svg>
      <span>+61 400 555 218</span>
    </div>
    <div class="contact__rule contact__rule--long"></div>
    <div class="contact__row">
      <svg viewBox="0 0 10 10"><rect x="0.5" y="2" width="9" height="6" fill="#2f74bd"/><path d="M0.5 2 L5 5.5 L9.5 2" fill="none" stroke="#fff" stroke-width="0.8"/></svg>
      <span>daniel.orwell@silverpine.com</span>
    </div>
    <div class="contact__rule contact__rule--short"></div>
    <div class="contact__row">
      <svg viewBox="0 0 10 10"><circle cx="5" cy="5" r="4.3" fill="none" stroke="#2f74bd" stroke-width="1"/><path d="M1 5 H9 M5 1 V9" stroke="#2f74bd" stroke-width="0.8"/></svg>
      <span>www.silverpine.com</span>
    </div>
  </div>

  <div class="brand brand--front">
    <span class="brand__dot"></span>
    <div class="brand__name">Silverpine<br>Thresholds</div>
  </div>
</section>

<section class="card card--back">
  <div class="brand brand--back">
    <span class="brand__dot"></span>
    <div class="brand__name">Silverpine Thresholds</div>
  </div>
  <div class="back-stripe"></div>
  <div class="back-band"></div>
</section>

</body>
</html>
```